I am looking for a graphic designer to create a Night Club flyer for an upcoming event. Here are the details for my event...

-Presented by Velvet Harbor Entertainment
-(night tittle) Copper Tide Jam
-(night will be themed around) DJ, Music, Lasers, Fog, and Gogo Dancers
-(target audience) European (DJ will be playing House, Indie Rock, Up Tempo Pop, International Dance Music, and so much more)
-Music by Live DJ (Playing nothing but the hottest hits!! or a statement of that nature)
-21 + Event / Proper ID is a Must
-For more info call / (508)-917-4280
-(venue) The Quarry / 17 Bramble Ln. Nantucket MA

```html
<!DOCTYPE html>
<html lang="en">
<head>
<meta charset="utf-8">
<title>Copper Tide Jam – Flyer</title>
<link rel="stylesheet" href="https://fonts.googleapis.com/css2?family=Russo+One&family=Open+Sans:wght@400;600&display=swap">
<style>
  :root {
    --page-bg: #d9dbe0;
    --flyer-deep: #3a0f5e;
    --flyer-mid: #7a2fb0;
    --flyer-bright: #b25ae0;
    --glow: #f4ecff;
    --teal: #2fd6c4;
    --teal-dark: #128a86;
    --violet-ink: #5a2a9a;
    --white: #ffffff;
  }
  * { margin: 0; padding: 0; box-sizing: border-box; }
  html, body { width: 1200px; height: 900px; overflow: hidden; }
  body {
    background: var(--page-bg);
    position: relative;
    font-family: "Open Sans", sans-serif;
  }
  .flyer {
    position: absolute;
    left: 290px; top: 20px;
    width: 620px; height: 860px;
    overflow: hidden;
    background:
      radial-gradient(circle at 50% 26%, var(--glow) 0, rgba(244,236,255,.75) 90px, rgba(178,90,224,.35) 220px, rgba(122,47,176,0) 340px),
      linear-gradient(180deg, var(--flyer-deep) 0%, var(--flyer-mid) 45%, var(--flyer-bright) 70%, var(--flyer-mid) 100%);
    box-shadow: 0 6px 18px rgba(0,0,0,.25);
  }
  .dance-floor {
    position: absolute;
    left: 0; bottom: 0;
    width: 100%; height: 440px;
    background: radial-gradient(ellipse at 50% 10%, rgba(255,210,255,.55) 0, rgba(214,120,240,.35) 40%, rgba(90,30,140,.2) 100%);
  }
  .dancer {
    position: absolute;
    left: 175px; top: 55px;
    width: 270px; height: 390px;
    border-radius: 48% 48% 12% 12%;
    background: linear-gradient(180deg, rgba(58,15,94,.85), rgba(90,42,154,.7));
  }
  .tagline {
    position: absolute;
    top: 28px;
    color: var(--white);
    font-size: 17px;
    line-height: 1.3;
  }
  .tagline--left { left: 26px; }
  .tagline--right { right: 26px; text-align: right; }
  .event-title {
    position: absolute;
    left: 0; top: 400px;
    width: 100%;
    text-align: center;
    font-family: "Russo One", sans-serif;
    font-size: 60px;
    line-height: 54px;
    text-transform: uppercase;
    color: var(--teal);
    text-shadow: 3px 3px 0 var(--violet-ink), 5px 5px 0 var(--teal-dark);
  }
  .presented-by {
    position: absolute;
    left: 0; top: 575px;
    width: 100%;
    text-align: center;
    font-family: "Russo One", sans-serif;
    font-size: 40px;
    line-height: 44px;
    color: var(--white);
    text-transform: uppercase;
  }
  .presenter {
    position: absolute;
    left: 0; top: 668px;
    width: 100%;
    text-align: center;
    font-family: "Russo One", sans-serif;
    font-size: 31px;
    color: var(--teal);
    text-transform: uppercase;
  }
  .event-info {
    position: absolute;
    left: 70px; top: 718px;
    color: var(--white);
    font-size: 18px;
    line-height: 1.45;
  }
</style>
</head>
<body>
  <main class="flyer">
    <div class="dance-floor" role="img" aria-label="Glowing dotted dance floor in purple and pink"></div>
    <div class="dancer" role="img" aria-label="Silhouette of a dancing woman in front of a bright light burst"></div>

    <p class="tagline tagline--left">DJ, Music, Lasers,<br>Fog, and Gogo Dancers</p>
    <p class="tagline tagline--right">Playing nothing<br>but the hottest hits!!</p>

    <h1 class="event-title">Copper<br>Tide<br>Jam</h1>
    <p class="presented-by">Presented<br>by</p>
    <p class="presenter">Velvet Harbor Entertainment</p>

    <p class="event-info">
      For more info call / (508)-917-4280<br>
      (venue) The Quarry / 17 Bramble Ln. Nantucket MA
    </p>
  </main>
</body>
</html>
```